Orvane Constructions Business card and Logo

We are a building company that would like our current logo design copied with the "Orvane Constructions" lines thicker.
We would also like our business cards copied with some minor copy changes. I have attached images of our logo and business cards.
We would like a standard size business card in landscape format rather than portrait.
On the back of the business card we would like a name added above the mobile number - "Remy Castellan"
Can I please get high res file of the logo and business cards at completion of redesign?

```html
<!DOCTYPE html>
<html lang="en">
<head>
<meta charset="utf-8">
<title>Orvane Constructions — Business Card</title>
<link rel="stylesheet" href="https://fonts.googleapis.com/css2?family=Source+Sans+3:wght@400;700&display=swap">
<style>
  :root {
    --green: #2bdb06;
    --blue: #0a14e6;
    --navy: #14148c;
    --ink: #111111;
    --white: #ffffff;
    --yellow: #f2e600;
    --border: #111111;
  }
  html, body {
    margin: 0;
    padding: 0;
    width: 1041px;
    height: 1200px;
    overflow: hidden;
    background: var(--white);
    font-family: "Source Sans 3", "Myriad Pro", Arial, sans-serif;
  }
  .canvas { position: relative; width: 1041px; height: 1200px; }

  .card {
    position: absolute;
    box-sizing: border-box;
    border: 2px solid var(--border);
    background: var(--white);
    overflow: hidden;
  }
  .card--front { left: 26px; top: 22px; width: 970px; height: 532px; }
  .card--back  { left: 28px; top: 628px; width: 971px; height: 531px; }

  .panel { position: absolute; left: 0; top: 0; display: block; }
  .card--front .panel { width: 966px; height: 474px; }
  .card--back .panel  { width: 608px; height: 488px; }

  .band { position: absolute; left: 0; background: var(--blue); }
  .card--front .band { top: 475px; width: 968px; height: 40px; }
  .card--back .band  { top: 489px; width: 967px; height: 37px; }

  .company-name {
    font-family: "Source Sans 3", Arial, sans-serif;
    font-weight: 700;
    fill: var(--white);
  }

  .details { position: absolute; left: 0; top: 0; width: 100%; height: 100%; }
  .name {
    position: absolute; left: 628px; top: 100px; margin: 0;
    font-size: 46px; font-weight: 400; color: var(--navy); line-height: 1;
    white-space: nowrap;
  }
  .address {
    position: absolute; left: 628px; top: 202px; margin: 0;
    font-size: 31px; color: var(--ink); line-height: 34px; font-style: normal;
  }
  .contact { position: absolute; left: 0; top: 308px; margin: 0; font-size: 27px; line-height: 32.5px; color: var(--ink); }
  .contact-row { display: flex; }
  .contact-label { width: 607px; text-align: right; margin: 0; }
  .contact-value { margin: 0; padding-left: 4px; white-space: nowrap; }
  .contact-value::before { content: ": "; }
  .acn {
    position: absolute; left: 628px; top: 451px; margin: 0;
    font-size: 30px; color: var(--ink); line-height: 1;
  }
  .abn {
    position: absolute; left: 628px; top: 495px; margin: 0;
    font-size: 26px; color: var(--yellow); line-height: 1;
  }
</style>
</head>
<body>
<main class="canvas">

  <section class="card card--front" aria-label="Card front">
    <svg class="panel" viewBox="0 0 966 474" role="img" aria-label="Green panel with faint architectural drawing of buildings in the background">
      <defs>
        <linearGradient id="frontGreen" x1="0" y1="0" x2="1" y2="1">
          <stop offset="0" stop-color="#2bdb06"/>
          <stop offset="0.5" stop-color="#35de14"/>
          <stop offset="1" stop-color="#2bdb06"/>
        </linearGradient>
      </defs>
      <rect width="966" height="474" fill="url(#frontGreen)"/>
      <text class="company-name" x="494" y="290" font-size="76" text-anchor="middle">Orvane Constructions</text>
    </svg>
    <div class="band"></div>
  </section>

  <section class="card card--back" aria-label="Card back">
    <svg class="panel" viewBox="0 0 608 488" role="img" aria-label="Green panel with faint architectural drawing of buildings in the background">
      <defs>
        <linearGradient id="backGreen" x1="0" y1="0" x2="1" y2="1">
          <stop offset="0" stop-color="#2bdb06"/>
          <stop offset="0.5" stop-color="#35de14"/>
          <stop offset="1" stop-color="#2bdb06"/>
        </linearGradient>
      </defs>
      <rect width="608" height="488" fill="url(#backGreen)"/>
      <text class="company-name" x="308" y="300" font-size="50" text-anchor="middle">Orvane Constructions</text>
    </svg>

    <div class="details">
      <h1 class="name">Remy Castellan</h1>
      <address class="address">PO Box 417<br>Kellbrook, Vic 3099</address>
      <dl class="contact">
        <div class="contact-row"><dt class="contact-label">Phone</dt><dd class="contact-value">0400 555 218</dd></div>
        <div class="contact-row"><dt class="contact-label">Fax</dt><dd class="contact-value">03 5550 1947</dd></div>
        <div class="contact-row"><dt class="contact-label">E-mail</dt><dd class="contact-value">admin@orvane.com.au</dd></div>
        <div class="contact-row"><dt class="contact-label">Web</dt><dd class="contact-value">orvane.com.au</dd></div>
      </dl>
      <p class="acn">ACN 04 618 293</p>
    </div>

    <div class="band"></div>
    <p class="abn">ABN 51104 618 293</p>
  </section>

</main>
</body>
</html>
```